Willowmere Spa and Beauty Ltd. (Name of business)

I need a business card designed for this new company based out of Toronto Ontario. We specialize in Eyelash Extensions, Manicures and Pedicures, body waxing, massages, laser hair removal and botox treatments. Also offer a variety of products for sale, such as skin cream serums, collagen gel, eye cream, etc. It is a safe relaxing and non-judgemental environnment. Clients are welcome to come be pampered for the half or full day. Many service packages to choose from.

Open 7days per week from 8am to 8pm.

Marissa Thornbury
Spa Facilitator
Willowmere Spa and Beauty Ltd.
7200 Calder Ave; Suite 1400
Toronto ON K8P 2W7

OFFICE: 416.739.4100
FAX: 416.739.4101
CELL: 416.582.6074
EMAIL: marissa.thornbury@willowmerespa.example

Target Market(s)

Target market is primarily female ranging from 16 years old to 50 years old.

Industry/Entity Type

Business

Contact Information for Business Card

Marissa Thornbury
Spa Facilitator
7200 Calder Ave; Suite 1400
Toronto ON K8P 2W7

OFFICE: 416.739.4100
FAX: 416.739.4101
CELL: 416.582.6074

Logo Text

I dont have a logo yet. I would like it simple but sophisticated and modern.

Font styles to use
Serif

Requirements
Must have
• all pertinent details such as company name, logo, name and contact information, services that are offered, including package rates
Nice to have
• Company name and logo prominent. A card that is neat and the information such as address, phone number, fax, email, etc is not too crowded but laid out in an easy to read format.
• Possibly on the back of card - some of the services offered could be listed, as well as professional cream lotions and serums. Hours of operation etc.

```html
<!DOCTYPE html>
<html lang="en">
<head>
<meta charset="utf-8">
<title>Willowmere Spa and Beauty Ltd. — Business Card</title>
<link rel="stylesheet" href="https://fonts.googleapis.com/css2?family=Open+Sans:wght@300;400;600;700&display=swap">
<style>
  :root {
    --backdrop: #3a322e;
    --card: #0d0d0d;
    --card-edge: #1c1c1c;
    --green: #3fa535;
    --green-deep: #2c7a25;
    --ink: #e9e9e9;
    --ink-soft: #cfcfcf;
  }
  * { box-sizing: border-box; margin: 0; padding: 0; }
  html, body { width: 1200px; height: 900px; overflow: hidden; }
  body {
    background: var(--backdrop);
    font-family: "Open Sans", Arial, sans-serif;
    position: relative;
  }
  .card {
    position: absolute;
    top: 301px;
    width: 520px;
    height: 297px;
    background: var(--card);
    border: 1px solid var(--card-edge);
    box-shadow: 0 6px 18px rgba(0,0,0,.45);
  }
  .card--contact { left: 50px; }
  .card--brand { left: 630px; }

  /* Contact side */
  .brand-mark {
    position: absolute;
    left: 28px; top: 128px;
    width: 200px;
    display: flex; align-items: center; gap: 10px;
  }
  .brand-mark__dot {
    width: 22px; height: 22px; border-radius: 50%;
    background: var(--green); flex: none;
  }
  .brand-mark__name {
    font-size: 24px; font-weight: 600; color: var(--green);
    letter-spacing: .5px;
  }
  .divider {
    position: absolute; left: 250px; top: 64px;
    width: 1px; height: 190px;
    background: linear-gradient(to bottom, transparent, var(--green-deep) 40%, var(--green-deep) 70%, transparent);
  }
  .details {
    position: absolute; left: 266px; top: 62px; right: 12px;
    color: var(--ink); font-size: 12px; line-height: 1.3;
  }
  .details__name { color: var(--green); font-weight: 700; font-size: 15px; line-height: 1.2; }
  .details__role { color: var(--ink-soft); margin-bottom: 12px; }
  .details__company { font-weight: 700; }
  .details__address { margin-bottom: 16px; }
  .contact-list { list-style: none; }
  .contact-list li { display: flex; align-items: center; gap: 8px; font-size: 12px; line-height: 1.45; }
  .contact-list li.email { font-size: 11px; }
  .contact-list svg { width: 10px; height: 10px; flex: none; fill: var(--green); }

  /* Brand side */
  .brand-lockup {
    position: absolute; left: 0; right: 0; top: 100px;
    display: flex; justify-content: center; align-items: center; gap: 12px;
  }
  .brand-lockup__dot { width: 26px; height: 26px; border-radius: 50%; background: var(--green); }
  .brand-lockup__name {
    font-size: 21px; font-weight: 600; color: var(--green);
    letter-spacing: 1.5px; text-transform: uppercase;
  }
  .hours {
    position: absolute; left: 0; right: 0; top: 190px;
    text-align: center; color: var(--green);
    font-size: 11px; letter-spacing: .6px; text-transform: uppercase;
  }
</style>
</head>
<body>
  <section class="card card--contact" aria-label="Contact side">
    <div class="brand-mark">
      <span class="brand-mark__dot"></span>
      <span class="brand-mark__name">Willowmere</span>
    </div>
    <div class="divider"></div>
    <div class="details">
      <p class="details__name">Marissa Thornbury</p>
      <p class="details__role">Spa Facilitator</p>
      <p class="details__company">Willowmere Spa and Beauty Ltd.</p>
      <p class="details__address">7200 Calder Ave; Suite 1400<br>Toronto ON K8P 2W7</p>
      <ul class="contact-list">
        <li><svg viewBox="0 0 10 10" aria-label="Office"><path d="M2 0.5 L3.6 2.6 L2.7 3.7 Q3.8 5.9 6.3 7.3 L7.4 6.4 L9.5 8 L8.2 9.5 Q4.5 9.2 2 6.6 Q0.2 4.3 0.5 1.6 Z"/></svg>416.739.4100</li>
        <li><svg viewBox="0 0 10 10" aria-label="Fax"><path d="M2.5 0.5h4.5l1 1v2.5h-5.5zM1 4.5h8v4.5h-8zM3 6h4v1h-4z" fill-rule="evenodd"/></svg>416.739.4101</li>
        <li><svg viewBox="0 0 10 10" aria-label="Cell"><path d="M2.5 0.5h5v9h-5zM3.3 1.5v6.2h3.4v-6.2z" fill-rule="evenodd"/></svg>416.582.6074</li>
        <li class="email"><svg viewBox="0 0 10 10" aria-label="Email"><path d="M0.5 2h9v6h-9zM1.4 2.7l3.6 2.8 3.6-2.8z" fill-rule="evenodd"/></svg>marissa.thornbury@willowmerespa.example</li>
      </ul>
    </div>
  </section>

  <section class="card card--brand" aria-label="Brand side">
    <div class="brand-lockup">
      <span class="brand-lockup__dot"></span>
      <span class="brand-lockup__name">Willowmere Spa and Beauty Ltd</span>
    </div>
    <p class="hours">Open 7days per week from 8am to 8pm.</p>
  </section>
</body>
</html>
```